Core Values Poster

I would like the layout I put together designed professionally. The poster will be vertical. I need two sizes 24" x 36" and 28" x 40". Convert the black and white poster into something colorful so that the icons pop and it is suitable for framing. The website is https://www.cedar4wellness.com/ for reference.

```html
<!DOCTYPE html>
<html lang="en">
<head>
<meta charset="utf-8">
<title>Core Values Poster</title>
<link href="https://fonts.googleapis.com/css2?family=Anton&family=Nunito:wght@800;900&family=Nunito+Sans:wght@400;600&display=swap" rel="stylesheet">
<style>
  :root {
    --backdrop: #c4c4c4;
    --paper: #fbf7f1;
    --peach: #fbe3c4;
    --gold: #c9a63e;
    --teal: #2faabf;
    --purple: #a598e6;
    --orange: #f07f1e;
    --green: #17944a;
    --blue: #0b80d3;
    --ink: #2b2b2b;
    --icon: #5a5a5a;
  }
  * { margin: 0; padding: 0; box-sizing: border-box; }
  html, body { width: 1200px; height: 2704px; overflow: hidden; background: var(--backdrop); }
  .poster {
    position: absolute; left: 50px; top: 527px; width: 1100px; height: 1650px;
    background:
      radial-gradient(ellipse 420px 520px at 0% 30%, var(--peach) 0%, transparent 70%),
      radial-gradient(ellipse 380px 520px at 100% 50%, var(--peach) 0%, transparent 70%),
      radial-gradient(ellipse 500px 300px at 30% 100%, #fdebd6 0%, transparent 70%),
      var(--paper);
    font-family: "Nunito Sans", sans-serif;
    color: var(--ink);
  }
  .brand { position: absolute; top: 80px; width: 100%; text-align: center; color: var(--gold); font-family: "Nunito Sans", sans-serif; font-weight: 400; }
  .brand-name { display: block; font-size: 128px; line-height: 1; letter-spacing: -2px; }
  .brand-sub { display: block; font-size: 46px; line-height: 1.2; letter-spacing: 4px; }
  .headline {
    position: absolute; top: 330px; width: 100%; text-align: center;
    font-family: "Anton", sans-serif; font-size: 112px; line-height: 1.05; letter-spacing: 3px;
    color: var(--blue);
  }
  .chain { position: absolute; left: 0; top: 0; }
  .value { position: absolute; }
  .value-title { font-family: "Nunito", sans-serif; font-weight: 900; font-size: 36px; line-height: 1; letter-spacing: .5px; }
  .value-list { list-style: none; margin-top: 12px; }
  .value-list li { font-size: 25px; line-height: 36px; font-weight: 600; position: relative; padding-left: 22px; }
  .value-list li::before { content: ""; position: absolute; left: 2px; top: 14px; width: 9px; height: 9px; border-radius: 50%; background: currentColor; }
  .value-list li span { color: var(--ink); }
  .dots { position: absolute; border-top: 4px dotted var(--ink); width: 60px; height: 0; top: 16px; }
  .value--right { left: 789px; }
  .value--right .dots { left: -74px; }
  .value--left { left: 80px; }
  .integrity { top: 553px; color: var(--gold); }
  .gratitude { top: 741px; color: var(--teal); }
  .innovation { top: 931px; color: var(--purple); }
  .energy { top: 1127px; color: var(--green); }
  .intelligence { top: 1326px; color: var(--orange); }
  .gratitude .dots { left: 276px; }
  .energy .dots { left: 202px; }
  .site {
    position: absolute; top: 1534px; width: 100%; text-align: center;
    font-size: 36px; letter-spacing: 5px; font-weight: 400;
  }
  .site-accent { color: var(--gold); }
</style>
</head>
<body>
<main class="poster">
  <header class="brand">
    <span class="brand-name">CEDAR4</span>
    <span class="brand-sub">WELLNESS</span>
  </header>
  <h1 class="headline">OUR CORE VALUES</h1>

  <svg class="chain" width="1100" height="1650" viewBox="0 0 1100 1650" aria-hidden="true">
    <defs>
      <filter id="soft-shadow" x="-30%" y="-30%" width="160%" height="160%">
        <feDropShadow dx="0" dy="4" stdDeviation="5" flood-color="#000" flood-opacity=".3"/>
      </filter>
    </defs>
    <g stroke-linecap="round" stroke-width="150" fill="none">
      <line class="band-gold" x1="624" y1="569" x2="429" y2="759" stroke="var(--gold)"/>
      <line class="band-orange" x1="432" y1="1140" x2="624" y2="1342" stroke="var(--orange)"/>
      <line class="band-teal" x1="429" y1="759" x2="627" y2="948" stroke="var(--teal)"/>
      <line class="band-purple" x1="627" y1="948" x2="432" y2="1140" stroke="var(--purple)"/>
    </g>
    <g fill="#f6f6f6" filter="url(#soft-shadow)">
      <circle cx="624" cy="569" r="57"/>
      <circle cx="429" cy="759" r="57"/>
      <circle cx="627" cy="948" r="57"/>
      <circle cx="432" cy="1140" r="57"/>
      <circle cx="624" cy="1342" r="57"/>
    </g>
    <g fill="var(--icon)" stroke="var(--icon)">
      <!-- handshake -->
      <g transform="translate(624 569)" stroke-width="0">
        <path d="M-38 -14 L-22 -20 L-6 -12 L4 -18 L22 -20 L38 -12 L38 8 L26 12 L10 24 Q4 28 -2 24 L-28 6 L-38 4 Z"/>
        <path d="M-4 -8 L8 2 L18 -2" fill="none" stroke="#f6f6f6" stroke-width="3"/>
      </g>
      <!-- hands with heart -->
      <g transform="translate(429 759)" stroke-width="0">
        <path d="M0 -8 C-4 -18 -20 -18 -20 -6 C-20 4 -8 10 0 18 C8 10 20 4 20 -6 C20 -18 4 -18 0 -8 Z" transform="translate(0 -12) scale(.75)"/>
        <path d="M-30 -6 L-24 -6 L-22 14 L-6 22 L-6 32 L-22 32 L-32 16 Z"/>
        <path d="M30 -6 L24 -6 L22 14 L6 22 L6 32 L22 32 L32 16 Z"/>
      </g>
      <!-- scales -->
      <g transform="translate(627 948)">
        <line x1="0" y1="-30" x2="0" y2="24" stroke-width="5"/>
        <line x1="-30" y1="-18" x2="30" y2="-18" stroke-width="4"/>
        <rect x="-18" y="22" width="36" height="8" stroke-width="0"/>
        <path d="M-42 6 L-30 -16 L-18 6 Z M18 6 L30 -16 L42 6 Z" fill="none" stroke-width="2.5"/>
        <path d="M-42 6 Q-30 18 -18 6 Z M18 6 Q30 18 42 6 Z" stroke-width="0"/>
        <circle cx="0" cy="-30" r="5" stroke-width="0"/>
      </g>
      <!-- bolt -->
      <g transform="translate(432 1140)" stroke-width="0">
        <path d="M6 -34 L-16 4 L-2 4 L-10 34 L16 -6 L2 -6 L14 -34 Z"/>
      </g>
      <!-- bulb with brain -->
      <g transform="translate(624 1342)">
        <circle cx="0" cy="-8" r="20" fill="none" stroke-width="4"/>
        <path d="M-6 -22 Q-14 -8 -4 0 M6 -22 Q14 -8 4 0 M0 -26 L0 8" fill="none" stroke-width="2.5"/>
        <rect x="-9" y="14" width="18" height="5" stroke-width="0"/>
        <rect x="-9" y="22" width="18" height="5" stroke-width="0"/>
        <rect x="-5" y="30" width="10" height="4" stroke-width="0"/>
        <path d="M0 -40 L0 -34 M-28 -8 L-34 -8 M28 -8 L34 -8 M-20 -28 L-24 -32 M20 -28 L24 -32" stroke-width="3" fill="none"/>
      </g>
    </g>
  </svg>

  <section class="value value--right integrity">
    <span class="dots"></span>
    <h2 class="value-title">INTEGRITY</h2>
    <ul class="value-list"><li><span>Dependability</span></li><li><span>Honesty</span></li><li><span>Loyalty</span></li></ul>
  </section>
  <section class="value value--left gratitude">
    <span class="dots"></span>
    <h2 class="value-title">GRATITUDE</h2>
    <ul class="value-list"><li><span>For Patients</span></li><li><span>For Coworkers</span></li><li><span>For Life</span></li></ul>
  </section>
  <section class="value value--right innovation">
    <span class="dots"></span>
    <h2 class="value-title">INNOVATION</h2>
    <ul class="value-list"><li><span>Dependability</span></li><li><span>Honesty</span></li><li><span>Loyalty</span></li></ul>
  </section>
  <section class="value value--left energy">
    <span class="dots"></span>
    <h2 class="value-title">ENERGY</h2>
    <ul class="value-list"><li><span>Body &amp; Mind</span></li><li><span>Be Proactive</span></li><li><span>It's Up to You</span></li></ul>
  </section>
  <section class="value value--right intelligence">
    <span class="dots"></span>
    <h2 class="value-title">INTELLIGENCE</h2>
    <ul class="value-list"><li><span>Know Your Duty</span></li><li><span>Continuous Learning</span></li><li><span>Always Ask</span></li></ul>
  </section>

  <footer class="site">WWW.<span class="site-accent">CEDAR4WELLNESS</span>.COM</footer>
</main>
</body>
</html>
```